New high end server provider needs wordpress design

www.kv7hostrack.com

Need a wordpress design for a high end server provider that provides overclocked dedicated servers for rent. We are located in Chicago but we have a presence is Virginia and Nevada for both our east and west coast customers.

We are a server provider that specializes in top end hardware with every feature designed for optimum performance. If it is not the best quality part or provides the best possible performance we don't run it. Our customers are mainly those that want the best single threaded performance possible from their hardware. We would be selling our services directly on our website via HostDesk.

We would like to see designs that are very modern and simplistic yet very attractive looking and catchy. Would prefer colors in the blues and greens and white. These colors are not necessary and I would be open to another color scheme if it looks good.

The final design should show speed and performance while being simplistic and easy on the eyes.
Updates

Logo and company name added and payment changed to guaranteed.  Looking for a wordpress template with the same pages as kv7hostrack.com but with a redesigned look and feel.  

HostDesk control panel design also part of the design request.

If you have any questions please let me know!  This is just for kv7hostrack.com and a main page for HostDesk (no coding just design).

Target Market(s)

IT Guru's (mostly men in their 20's to 30's)

Industry/Entity Type

Hardware

Requirements
Must have
• HostDesk panel design to fit with website theme.
Nice to have
• Main slider on home page similar to one of our other websites at www.kv7hostrack.com
Should not have
• Flash or frames

```html
<!DOCTYPE html>
<html lang="en"><head><meta charset="utf-8"><title>KV7HostRack Admin Summary</title>
<link href="https://fonts.googleapis.com/css2?family=Open+Sans:wght@400;600;700&display=swap" rel="stylesheet">
<style>
:root{--topbar:#4ea7d0;--dark:#2a2f35;--tab:#1d2227;--page:#e9e9e9;--card:#fff;--panel:#f1f1f1;--head:#3a7ea3;--text:#333;--link:#2a8bc4;--muted:#777;--green:#3aa845;--red:#e23b2a;--orange:#d48a00;--olive:#6e8f12;--th:#c9cbcc;--line:#d6d6d6}
*{box-sizing:border-box;margin:0;padding:0}
html,body{width:1200px;height:2202px;overflow:hidden}
body{font-family:"Open Sans",Arial,sans-serif;font-size:11px;color:var(--text);background:var(--page);position:relative}
a{color:var(--link);text-decoration:none}
.topbar{position:absolute;top:0;left:0;width:1200px;height:20px;background:var(--topbar);color:#fff;font-size:11px;line-height:20px;padding:0 16px;display:flex;justify-content:space-between}
.topbar a{color:#fff}
.masthead{position:absolute;top:20px;left:0;width:1200px;height:70px;background:var(--dark)}
.brand{position:absolute;left:24px;top:18px;color:#dfe6ea;font-size:22px;font-weight:700;letter-spacing:1px;display:flex;align-items:center;gap:8px}
.brand i{width:16px;height:16px;border-radius:50%;background:#9fb6c4;display:block}
.alerts{position:absolute;top:9px;left:0;width:1200px;text-align:center;color:#ccc;font-size:10.5px}
.alerts b{color:#7fc2e4;font-weight:400}
.search{position:absolute;right:16px;top:10px;width:124px;height:20px;background:#454b52;border-radius:3px;color:#9aa;font-size:10px;line-height:20px;padding-left:6px}
.tabs{position:absolute;top:43px;left:355px;display:flex;gap:3px}
.tabs span{background:var(--tab);color:#fff;font-size:10.5px;font-weight:600;padding:0 12px;height:27px;line-height:27px;border:1px solid #4b535b;border-bottom:0;border-radius:3px 3px 0 0}
.shortcuts{position:absolute;top:90px;left:0;width:1200px;height:24px;background:#fff;border-bottom:1px solid #ddd;font-size:10px;line-height:24px;padding-left:16px}
.shortcuts a{margin-right:14px}
.shortcuts a::before{content:"";display:inline-block;width:8px;height:8px;background:#9cc6de;margin-right:4px;vertical-align:-1px}
.main{position:absolute;top:126px;left:16px;width:1168px;height:2045px;background:var(--card)}
.title{position:absolute;left:39px;top:148px;font-size:15px;font-weight:700;color:#222}
.welcome{position:absolute;left:39px;top:187px;font-size:10px}
.income{position:absolute;right:40px;top:149px;font-size:14px;font-weight:600;color:#444}
.income .a{color:var(--link);font-weight:400}.income .b{color:var(--green);font-weight:400}.income .c{color:var(--red);font-weight:400}
.panel{position:absolute;width:551px;background:var(--panel)}
.panel.l{left:39px}.panel.r{left:610px}
.ph{height:24px;background:var(--head);color:#fff;font-weight:700;font-size:11.5px;line-height:24px;padding-left:30px;position:relative}
.ph::before{content:"";position:absolute;left:10px;top:7px;width:11px;height:10px;background:#f0c040;border-radius:2px}
.ph::after{content:"";position:absolute;right:10px;top:11px;width:10px;height:2px;background:#fff}
.pb{padding:12px 16px;position:relative}
table{border-collapse:collapse;background:#fff;font-size:10px}
th{background:var(--th);text-align:left;font-weight:600;padding:0 8px;height:20px;color:#333}
td{padding:0 8px;height:17px;border-right:1px solid var(--line)}
tbody tr:first-child td{padding-top:6px;height:23px}
.ed{width:10px;height:10px;background:#8bbcd8;display:inline-block}
.more{text-align:right;font-size:10px;margin-top:8px}
.kv{display:grid;grid-template-columns:100px 190px 80px 1fr;row-gap:3px;font-size:10px}
.stats{display:grid;grid-template-columns:36px 200px 36px 1fr;row-gap:7px;font-size:10px;padding:4px 18px}
.stats b{text-align:center}
.lastlogin{background:#b3b5b7;color:#fff;text-align:center;font-size:10px;height:20px;line-height:20px;margin-top:14px}
.feed p{font-size:10px;line-height:14px;margin-bottom:5px}
.follow{position:absolute;right:16px;top:12px;background:#fff;border:1px solid #ccc;padding:2px 8px;font-weight:600;font-size:11px}
.log p{font-size:10px;line-height:14px;margin-bottom:10px}
.fc{display:grid;grid-template-columns:1fr 1fr;padding:6px 57px}
.fc h4{color:var(--link);font-size:10.5px;margin-bottom:4px}
.fc div div{display:grid;grid-template-columns:80px 1fr;font-size:10px;line-height:18.5px}
.fc .est{color:var(--olive);font-weight:700}
.notes{background:#fff;border:1px solid #ccc;height:92px;margin:8px 18px 0;padding:10px 14px;font-size:10px}
.btn{position:absolute;right:36px;bottom:12px;background:#4a4f55;color:#fff;font-size:10px;padding:3px 10px}
.footer{position:absolute;bottom:0;left:0;width:1200px;height:24px;background:var(--dark);color:#aab;font-size:10px;line-height:24px;padding:0 16px;display:flex;justify-content:space-between}
</style></head><body>
<div class="topbar"><span><a>Home</a> | <a>Client Area</a> | <a>My Notes</a> | <a>My Account</a> | <a>Logout</a></span><span>Tuesday, 19 February 2013, 10:52</span></div>
<header class="masthead">
<div class="brand"><i></i>KV7HOSTRACK</div>
<div class="alerts"><b>3</b> Pending Orders | <b>34</b> Overdue Invoices | <b>0</b> Ticket(s) Awaiting Reply</div>
<div class="search">Search here...</div>
<nav class="tabs"><span>Clients</span><span>Orders</span><span>Billing</span><span>Support</span><span>Reports</span><span>Utilities</span><span>Addons</span><span>Setup</span><span>Help</span></nav>
</header>
<div class="shortcuts">Shortcuts: <a>Add New Client</a><a>Add New Order</a><a>Create New Quote</a><a>Create New To-Do Entry</a><a>Open New Ticket</a><a>WHOIS Lookup</a><a>Generate Due Invoices</a><a>Attempt CC Captures</a></div>
<div class="main"></div>
<h1 class="title">Admin Summary</h1>
<div class="welcome">Welcome Back Admin User!</div>
<div class="income">Income Today: <span class="a">RS 0.00</span> This Month: <span class="b">RS 48,993,525.43</span> This Year: <span class="c">RS 512,845,761.33</span></div>

<section class="panel l" style="top:217px;height:94px"><div class="ph">System Information</div><div class="pb"><div class="kv">
<span>Registered To:</span><span>HostDesk Demo</span><span>Expires:</span><span>Never</span>
<span>License Type:</span><span>Owned License</span><span>Version:</span><span>5.0.2 <b style="color:var(--red);font-weight:600">An update is available!</b></span>
<span>Staff Online:</span><span>Admin</span></div></div></section>

<section class="panel l" style="top:329px;height:92px"><div class="ph">PayRelay Overview</div><div class="pb" style="font-size:10px">Lookup PayRelay Transaction ID: <span style="display:inline-block;width:230px;height:18px;background:#e2e4e4;color:#888;padding:2px 6px;vertical-align:middle">102589664</span> <span style="display:inline-block;width:22px;height:18px;background:#444;vertical-align:middle"></span><div class="more"><a>Advanced Search »</a></div></div></section>

<section class="panel l" style="top:440px;height:178px"><div class="ph">Recent Client Activity</div><div class="pb" style="padding:18px 0 0 82px"><table style="width:370px"><thead><tr><th>Client IP</th><th>Address</th><th>Last Access</th></tr></thead><tbody>
<tr><td><a>demo demo</a></td><td><a>203.0.113.36</a></td><td>19/02/2013 10:48</td></tr>
<tr><td><a>Tio Prana</a></td><td><a>198.51.100.195</a></td><td>19/02/2013 10:13</td></tr>
<tr><td><a>dean bale</a></td><td><a>192.0.2.3</a></td><td>18/02/2013 20:13</td></tr>
<tr><td><a>shaw ko</a></td><td><a>198.51.100.63</a></td><td>18/02/2013 11:48</td></tr>
<tr><td><a>sysra sysra</a></td><td><a>203.0.113.174</a></td><td>18/02/2013 08:56</td></tr></tbody></table></div></section>

<section class="panel l" style="top:637px;height:228px"><div class="ph">System Overview</div><div class="pb"><div class="stats">
<b>4</b><span>New Orders Today</span><b style="color:var(--olive)">203</b><span>Active Clients</span>
<b>11</b><span>New Orders Yesterday</span><b style="color:var(--olive)">10</b><span>Active Services</span>
<b style="color:var(--orange)">3</b><span>Todays Pending Orders</span><b style="color:var(--red)">34</b><span>Overdue Invoices</span>
<b style="color:var(--red)">1</b><span>Todays Accepted Orders</span><b style="color:var(--orange)">0</b><span>Pending Cancellation(s)</span>
<b style="color:var(--red)">0</b><span>Ticket(s) Awaiting Reply</span><b>86</b><span>Valid Quotes</span>
<b>0</b><span>My Flagged Tickets</span><b>20</b><span>Uninvoiced Billable Items</span></div>
<div class="lastlogin">Your Last Login: <b>19/02/2013</b> 10:51 from IP <b>198.51.100.59</b></div></div></section>

<section class="panel l" style="top:882px;height:176px"><div class="ph">Recent Admin Activity</div><div class="pb" style="padding:18px 0 0 82px"><table style="width:370px"><thead><tr><th>Admin</th><th>IP Address</th><th>Last Access</th></tr></thead><tbody>
<tr><td><a>Admin</a></td><td><a>192.0.2.66</a></td><td>19/02/2013 10:52</td></tr>
<tr><td><a>Admin</a></td><td><a>198.51.100.59</a></td><td>19/02/2013 10:51</td></tr>
<tr><td><a>Admin</a></td><td><a>203.0.113.113</a></td><td>19/02/2013 10:49</td></tr>
<tr><td><a>Admin</a></td><td><a>192.0.2.242</a></td><td>19/02/2013 10:49</td></tr>
<tr><td><a>Admin</a></td><td><a>203.0.113.113</a></td><td>19/02/2013 10:49</td></tr></tbody></table></div></section>

<section class="panel l" style="top:1082px;height:263px"><div class="ph">HostDesk News Feed</div><div class="pb feed"><span class="follow">Follow Us <a>@hostdesk</a></span>
<p><b>Sunday, February 10th, 2013</b><br>@thecubex HostDesk :)</p>
<p><b>Sunday, February 10th, 2013</b><br>PluginYard's Guest Blog Post gets you coding <a>http://hd.link/cs06lwt</a></p>
<p><b>Thursday, January 31st, 2013</b><br>HostDesk 5.2 Closed Beta Opens Friday! Find out more at <a>http://hd.link/k82A5wdT</a></p>
<p><b>Wednesday, January 30th, 2013</b><br>The HostDesk Team will be attending the Cloudworks Summit next week. Are you? #CloudworksSummit</p>
<p><b>Sunday, January 27th, 2013</b><br>Have you taken our latest survey? Our UI Team is working on new order forms &amp; cart processes, but we need your help. <a>http://hd.link/DUzgljY</a></p>
<p><b>Monday, January 21st, 2013</b><br>Another issue of HostDesk Insights - Email Marketer tool <a>http://hd.link/Na6G4Ay6</a></p></div></section>

<section class="panel l" style="top:1365px;height:192px"><div class="ph">My Notes</div><div class="notes">thenightcrew.com/\nSay no to crews</div><span class="btn">Save Notes</span></section>

<section class="panel l" style="top:1574px;height:203px"><div class="ph">Income Forecast</div><div class="pb fc">
<div><h4>PKR Currency</h4><div><span>Monthly:</span><span>RS 0.00 (0)</span><span>Quarterly:</span><span>RS 0.00 (0)</span><span>Semi-Annually:</span><span>RS 0.00 (0)</span><span>Annually:</span><span>RS 0.00 (0)</span><span>Biennially:</span><span>RS 0.00 (0)</span><span>Triennially:</span><span>RS 0.00 (0)</span><span class="est">Est. Annual:</span><span class="est">RS 0.00</span></div></div>
<div><h4>CHF Currency</h4><div><span>Monthly:</span><span>CHF0.00 (0)</span><span>Quarterly:</span><span>CHF0.00 (0)</span><span>Semi-Annually:</span><span>CHF0.00 (0)</span><span>Annually:</span><span>CHF0.00 (0)</span><span>Biennially:</span><span>CHF0.00 (0)</span><span>Triennially:</span><span>CHF0.00 (0)</span><span class="est">Est. Annual:</span><span class="est">CHF0.00</span></div></div></div></section>

<section class="panel l" style="top:1804px;height:272px"><div class="ph">Orders Overview</div><div class="pb" style="padding:22px 0 0 86px">
<svg width="380" height="202" viewBox="0 0 380 202" font-family="Open Sans, sans-serif" font-size="7">
<rect width="380" height="202" fill="#fff" stroke="#ccc"/>
<text x="30" y="14" font-size="8">Orders Performance</text>
<rect x="290" y="8" width="5" height="5" fill="#2f5db8"/><text x="297" y="13">2013</text><rect x="318" y="8" width="5" height="5" fill="#d8291f"/><text x="325" y="13">2012</text>
<g stroke="#e2e2e2"><line x1="30" y1="30" x2="370" y2="30"/><line x1="30" y1="50" x2="370" y2="50"/><line x1="30" y1="70" x2="370" y2="70"/><line x1="30" y1="90" x2="370" y2="90"/><line x1="30" y1="110" x2="370" y2="110"/><line x1="30" y1="130" x2="370" y2="130"/><line x1="30" y1="150" x2="370" y2="150"/></g>
<g stroke="#e2e2e2"><line x1="58" y1="24" x2="58" y2="170"/><line x1="86" y1="24" x2="86" y2="170"/><line x1="114" y1="24" x2="114" y2="170"/><line x1="142" y1="24" x2="142" y2="170"/><line x1="170" y1="24" x2="170" y2="170"/><line x1="198" y1="24" x2="198" y2="170"/><line x1="226" y1="24" x2="226" y2="170"/><line x1="254" y1="24" x2="254" y2="170"/><line x1="282" y1="24" x2="282" y2="170"/><line x1="310" y1="24" x2="310" y2="170"/><line x1="338" y1="24" x2="338" y2="170"/></g>
<line x1="30" y1="170" x2="370" y2="170" stroke="#888"/><line x1="30" y1="24" x2="30" y2="170" stroke="#888"/>
<g text-anchor="end"><text x="27" y="32">16</text><text x="27" y="52">14</text><text x="27" y="72">12</text><text x="27" y="92">10</text><text x="27" y="112">8</text><text x="27" y="132">6</text><text x="27" y="152">4</text><text x="27" y="172">0</text></g>
<rect x="60" y="35" width="20" height="135" fill="#2f5db8"/><text x="70" y="32" text-anchor="middle">15</text>
<g text-anchor="middle" fill="#555"><text x="44" y="167">00</text><text x="100" y="167">00</text><text x="128" y="167">00</text><text x="156" y="167">00</text><text x="184" y="167">00</text><text x="212" y="167">00</text><text x="240" y="167">00</text><text x="268" y="167">00</text><text x="296" y="167">00</text><text x="324" y="167">00</text><text x="352" y="167">00</text></g>
<g fill="#555"><text transform="translate(46,196) rotate(-90)">Jan</text><text transform="translate(74,196) rotate(-90)">Feb</text><text transform="translate(102,196) rotate(-90)">Mar</text><text transform="translate(130,196) rotate(-90)">Apr</text><text transform="translate(158,196) rotate(-90)">May</text><text transform="translate(186,196) rotate(-90)">Jun</text><text transform="translate(214,196) rotate(-90)">Jul</text><text transform="translate(242,196) rotate(-90)">Aug</text><text transform="translate(270,196) rotate(-90)">Sep</text><text transform="translate(298,196) rotate(-90)">Oct</text><text transform="translate(326,196) rotate(-90)">Nov</text><text transform="translate(354,196) rotate(-90)">Dec</text></g>
</svg></div></section>

<section class="panel r" style="top:219px;height:202px"><div class="ph">Open Invoices</div><div class="pb" style="padding:18px 16px 0"><table style="width:516px"><thead><tr><th>Invoice #</th><th>Client Name</th><th>Invoice Date</th><th>Due Date</th><th>Total Due</th><th>Payment Method</th><th></th></tr></thead><tbody>
<tr><td>101010</td><td>asha remy</td><td>12/02/2013</td><td>12/02/2013</td><td>RS 0.00</td><td>PayRelay</td><td><i class="ed"></i></td></tr>
<tr><td>101010</td><td></td><td>12/02/2013</td><td>12/02/2013</td><td>RS 0.00</td><td>CoinPurse</td><td><i class="ed"></i></td></tr>
<tr><td>101010</td><td>test test</td><td>12/02/2013</td><td>12/02/2013</td><td>RS 80.00</td><td>QuickCheckout</td><td><i class="ed"></i></td></tr>
<tr><td>101010</td><td>Omar Ali Basri</td><td>14/02/2013</td><td>14/02/2013</td><td>$12.00</td><td>CoinPurse</td><td><i class="ed"></i></td></tr>
<tr><td>101010</td><td>Lena Varga</td><td>14/02/2013</td><td>14/02/2013</td><td>RS 221.00</td><td>CoinPurse</td><td><i class="ed"></i></td></tr></tbody></table><div class="more"><a>View All »</a></div></div></section>

<section class="panel r" style="top:440px;height:283px"><div class="ph">To Do List</div><div class="pb" style="padding:18px 16px 0"><table style="width:516px"><thead><tr><th>Date</th><th>Title/Description</th><th>Due Date</th><th>Status</th><th></th></tr></thead><tbody>
<tr><td>09/02/2013</td><td>Test To Do - Prepare Sales Brochures</td><td>10/02/2013</td><td>New</td><td><i class="ed"></i></td></tr>
<tr><td>11/02/2013</td><td>Manual Upgrade Required - Manual Upgrade Req.</td><td>11/02/2013</td><td>Pending</td><td><i class="ed"></i></td></tr>
<tr><td>11/02/2013</td><td>Manual Upgrade Required - Manual Upgrade Req.</td><td>11/02/2013</td><td>Pending</td><td><i class="ed"></i></td></tr>
<tr><td>13/02/2013</td><td>Manual Domain Registration - Client ID 5 has paid.</td><td>13/02/2013</td><td>Pending</td><td><i class="ed"></i></td></tr>
<tr><td>13/02/2013</td><td>Manual Domain Transfer - Client ID 210 has paid.</td><td>13/02/2013</td><td>Pending</td><td><i class="ed"></i></td></tr>
<tr><td>13/02/2013</td><td>Manual Upgrade Required - Manual Upgrade Req.</td><td>13/02/2013</td><td>Pending</td><td><i class="ed"></i></td></tr>
<tr><td>13/02/2013</td><td>Manual Upgrade Required - Manual Upgrade Req.</td><td>13/02/2013</td><td>Pending</td><td><i class="ed"></i></td></tr>
<tr><td>09/02/2013</td><td>teste - testando</td><td>16/02/2013</td><td>New</td><td><i class="ed"></i></td></tr>
<tr><td>15/02/2013</td><td>Domain Pending Transfer - Check the transfer stat...</td><td>20/02/2013</td><td>In Progress</td><td><i class="ed"></i></td></tr></tbody></table><div class="more"><a>Manage »</a></div></div></section>

<section class="panel r" style="top:745px;height:261px"><div class="ph">Income Overview</div><div class="pb" style="padding:22px 0 0 126px">
<svg width="300" height="196" viewBox="0 0 300 196" font-family="Open Sans, sans-serif" font-size="7">
<rect width="300" height="196" fill="#fff" stroke="#ccc"/>
<text x="40" y="18" font-size="7.5">Daily Income Comparison for the Past 2 Weeks</text>
<rect x="232" y="12" width="5" height="5" fill="#2f5db8"/><text x="239" y="17">Week 08</text><rect x="266" y="12" width="5" height="5" fill="#d8291f"/><text x="273" y="17">Week 7</text>
<g stroke="#e2e2e2"><line x1="40" y1="40" x2="290" y2="40"/><line x1="40" y1="60" x2="290" y2="60"/><line x1="40" y1="80" x2="290" y2="80"/><line x1="40" y1="100" x2="290" y2="100"/><line x1="40" y1="120" x2="290" y2="120"/><line x1="40" y1="140" x2="290" y2="140"/><line x1="40" y1="160" x2="290" y2="160"/><line x1="76" y1="30" x2="76" y2="180"/><line x1="112" y1="30" x2="112" y2="180"/><line x1="148" y1="30" x2="148" y2="180"/><line x1="184" y1="30" x2="184" y2="180"/><line x1="220" y1="30" x2="220" y2="180"/><line x1="256" y1="30" x2="256" y2="180"/></g>
<line x1="40" y1="180" x2="290" y2="180" stroke="#888"/><line x1="40" y1="30" x2="40" y2="180" stroke="#888"/>
<g text-anchor="end" fill="#555"><text x="37" y="42">300000</text><text x="37" y="62">250000</text><text x="37" y="82">200000</text><text x="37" y="102">150000</text><text x="37" y="122">100000</text><text x="37" y="142">50000</text><text x="37" y="182">0</text></g>
<rect x="230" y="40" width="18" height="140" fill="#d8291f" stroke="#a01810"/>
<g fill="#555"><text x="45" y="177">12736.00</text><text x="150" y="177">12345.00</text><text x="190" y="177">3780000</text><text x="262" y="177">1690.00</text><text x="239" y="37" text-anchor="middle">48939672.00</text></g>
<g text-anchor="middle" fill="#555"><text x="58" y="190">Wed</text><text x="94" y="190">Thu</text><text x="130" y="190">Fri</text><text x="166" y="190">Sat</text><text x="202" y="190">Sun</text><text x="238" y="190">Mon</text><text x="274" y="190">Tue</text></g>
</svg></div></section>

<section class="panel r" style="top:1038px;height:417px"><div class="ph">Activity Log</div><div class="pb log">
<p>Access Denied to View Email Message Log<br>&nbsp;- 19/02/2013 10:29 - Sales - 198.51.100.179</p>
<p>Access Denied to View Billable Items<br>&nbsp;- 19/02/2013 10:29 - Sales - 198.51.100.179</p>
<p>Order ID 569 Passed Fraud Check<br>&nbsp;- 19/02/2013 10:27 - Client - 198.51.100.179</p>
<p>Order ID 569 Fraud Check Awaiting User Input<br>&nbsp;- 19/02/2013 10:27 - Client - 198.51.100.179</p>
<p>Order ID 569 Fraud Check Initiated<br>&nbsp;- 19/02/2013 10:27 - Client - 198.51.100.179</p>
<p>Email Sent to demo demo (Order Confirmation)<br>&nbsp;- 19/02/2013 10:27 - Client - 198.51.100.179</p>
<p>Email Sent to demo demo (Customer Invoice)<br>&nbsp;- 19/02/2013 10:27 - Client - 198.51.100.179</p>
<p>Created Invoice - Invoice ID: 922<br>&nbsp;- 19/02/2013 10:27 - Client - 198.51.100.179</p>
<p>Email Sent to demo demo (Invoice Payment Confirmation)<br>&nbsp;- 19/02/2013 10:27 - Client - 198.51.100.179</p>
<p>Invoice Marked Paid - Invoice ID: 921<br>&nbsp;- 19/02/2013 10:27 - Client - 198.51.100.179</p>
<div class="more" style="margin-top:0"><a>View All »</a></div></div></section>

<section class="panel r" style="top:1478px;height:236px"><div class="ph">Network Status</div><div class="pb" style="padding:18px 16px 0"><table style="width:516px"><thead><tr><th>Server Name</th><th>HTTP</th><th>Load</th><th>Uptime</th><th>% Used</th></tr></thead><tbody>
<tr><td>-</td><td>-</td><td>-</td><td>-</td><td>0%</td></tr>
<tr><td>Administrator</td><td>-</td><td>-</td><td>-</td><td>1%</td></tr>
<tr><td>NorthBeatFM</td><td>-</td><td>-</td><td>-</td><td>0%</td></tr>
<tr><td>DeLunaonline</td><td>-</td><td>-</td><td>-</td><td>0%</td></tr>
<tr><td>node</td><td>-</td><td>-</td><td>-</td><td>0%</td></tr>
<tr><td>node</td><td>-</td><td>-</td><td>-</td><td>0%</td></tr>
<tr><td>node24</td><td>-</td><td>-</td><td>-</td><td>0%</td></tr></tbody></table><div class="more"><a>Check Now »</a></div></div></section>

<footer class="footer"><span>Staff Online: Admin</span><span>Copyright © KV7HostRack. All Rights Reserved.</span></footer>
</body></html>
```